Brisk Lantern Accounting - New client package

I need a stationary package (presentation folder cover, welcome letter template/design, sample financial report template/design, business card and new logo) for my accounting business. I would like to see designs that use the color blue. Financial icons can be included in the design. The final design should be clean and communicate professionalism and the use of modern; user-friendly technology. Attached postcard files should help with overall design concept.

```html
<!DOCTYPE html>
<html lang="en">
<head>
<meta charset="utf-8">
<title>Brisk Lantern Accounting – Business Card</title>
<link href="https://fonts.googleapis.com/css2?family=Tinos:wght@400;700&family=Montserrat:wght@400&display=swap" rel="stylesheet">
<style>
  :root {
    --navy-top: #034e77;
    --navy-bottom: #05334f;
    --navy: #0a4166;
    --blue: #1f6aa5;
    --white: #ffffff;
    --stage: #dcdcdc;
    --ink: #1d4c78;
  }
  * { box-sizing: border-box; margin: 0; padding: 0; }
  html, body {
    width: 1089px; height: 1200px; overflow: hidden;
    background: var(--stage);
  }
  .sheet { position: relative; width: 1089px; height: 1200px; }
  .card {
    position: absolute; left: 104px; width: 880px; height: 503px;
    box-shadow: 0 6px 18px rgba(0,0,0,0.22);
    overflow: hidden;
  }
  .card-front { top: 52px; background: linear-gradient(180deg, var(--navy-top), var(--navy-bottom)); }
  .card-back { top: 630px; background: var(--white); }

  .edge-bar { position: absolute; left: 292px; width: 295px; height: 13px; }
  .card-front .edge-bar { background: var(--white); }
  .card-back .edge-bar { background: var(--navy); }
  .edge-bar.top { top: 0; }
  .edge-bar.bottom { bottom: 0; }

  .front-brand {
    position: absolute; left: 0; right: 0; top: 200px;
    display: flex; justify-content: center; align-items: center; gap: 18px;
    font-family: "Tinos", "Times New Roman", serif;
    font-size: 54px; color: var(--white);
  }
  .brand-square { width: 26px; height: 26px; background: currentColor; flex: none; }
  .front-web {
    position: absolute; left: 120px; top: 440px;
    font-family: "Montserrat", Arial, sans-serif;
    font-size: 19px; letter-spacing: 6.2px; color: var(--white);
  }

  .back-tab {
    position: absolute; left: 370px; top: 0; width: 47px; height: 168px;
    background: var(--navy); border-radius: 0 0 24px 24px;
  }
  .back-brand {
    position: absolute; left: 24px; top: 200px; width: 320px;
    display: flex; align-items: center; gap: 14px;
    font-family: "Tinos", "Times New Roman", serif;
    font-size: 33px; line-height: 1.1; color: var(--blue);
  }
  .back-brand .brand-square { width: 20px; height: 20px; }

  .contact { position: absolute; left: 370px; display: flex; align-items: center; gap: 14px; }
  .contact .icon {
    width: 47px; height: 47px; border-radius: 50%; background: var(--navy);
    display: flex; align-items: center; justify-content: center; flex: none;
  }
  .card-back .contact.name { top: 116px; }
  .contact.name .icon { background: transparent; }
  .person-name {
    font-family: "Tinos", "Times New Roman", serif; font-weight: 700;
    font-size: 40px; letter-spacing: 1px; color: var(--navy);
  }
  .person-name .surname { color: var(--blue); }
  .contact-text {
    font-family: "Tinos", "Times New Roman", serif;
    font-size: 27px; color: var(--ink);
  }
  .row-1 { top: 188px; }
  .row-2 { top: 251px; }
  .row-3 { top: 312px; }
  .row-4 { top: 376px; }
</style>
</head>
<body>
<main class="sheet">
  <section class="card card-front" aria-label="Business card front">
    <div class="edge-bar top"></div>
    <div class="front-brand"><span class="brand-square"></span>Brisk Lantern Accounting</div>
    <p class="front-web">WWW.BRISKLANTERNACCOUNTING.COM</p>
    <div class="edge-bar bottom"></div>
  </section>

  <section class="card card-back" aria-label="Business card back">
    <div class="back-tab"></div>
    <div class="back-brand"><span class="brand-square"></span><span>Brisk Lantern<br>Accounting</span></div>

    <div class="contact name">
      <span class="icon">
        <svg width="26" height="30" viewBox="0 0 26 30"><circle cx="13" cy="8" r="7" fill="#fff"/><path d="M1 29c0-8 5-12 12-12s12 4 12 12z" fill="#fff"/></svg>
      </span>
      <span class="person-name">MAREN <span class="surname">HOLLOWAY</span></span>
    </div>

    <div class="contact row-1">
      <span class="icon">
        <svg width="24" height="24" viewBox="0 0 24 24"><path d="M6.6 10.8a15 15 0 0 0 6.6 6.6l2.2-2.2c.3-.3.7-.4 1-.2 1.1.4 2.3.6 3.6.6.6 0 1 .4 1 1V20c0 .6-.4 1-1 1A17 17 0 0 1 3 4c0-.6.4-1 1-1h3.5c.6 0 1 .4 1 1 0 1.3.2 2.5.6 3.6.1.3 0 .7-.2 1z" fill="#fff"/></svg>
      </span>
      <span class="contact-text">1.800.555.0142</span>
    </div>
    <div class="contact row-2">
      <span class="icon">
        <svg width="20" height="28" viewBox="0 0 20 28"><rect x="3" y="1" width="14" height="26" rx="3" fill="none" stroke="#fff" stroke-width="2"/><rect x="6" y="5" width="8" height="15" fill="#fff"/><circle cx="10" cy="23" r="1.4" fill="#fff"/></svg>
      </span>
      <span class="contact-text">415.555.0187</span>
    </div>
    <div class="contact row-3">
      <span class="icon">
        <svg width="28" height="20" viewBox="0 0 28 20"><rect x="1" y="1" width="26" height="18" fill="none" stroke="#fff" stroke-width="2"/><path d="M1 1l13 10L27 1M1 19l10-9M27 19l-10-9" fill="none" stroke="#fff" stroke-width="2"/></svg>
      </span>
      <span class="contact-text">Maren@BriskLanternAccounting.com</span>
    </div>
    <div class="contact row-4">
      <span class="icon">
        <svg width="28" height="28" viewBox="0 0 28 28"><g fill="none" stroke="#fff" stroke-width="1.6"><circle cx="14" cy="14" r="12"/><ellipse cx="14" cy="14" rx="5.5" ry="12"/><path d="M2 14h24M4 8h20M4 20h20M14 2v24"/></g></svg>
      </span>
      <span class="contact-text">www.brisklanternaccounting.com</span>
    </div>

    <div class="edge-bar bottom"></div>
  </section>
</main>
</body>
</html>
```